Minimalistic and chic product labels required for tea packaging

We need a Label Sticker Design for our tea company that is minimalistic, simple and chic.

We have 2 categories of tea: artisan tea (single flavoured tea e.g. green and black) and herbal teas (e.g. mixuture of herbs and flowers). We would like to have the designs to tell the difference of artisan tea and herbal tea, this can be done by having different colours to tell the difference or if there are other design features used.

We would also like to have colourful colours on our herbal tea range, preferably either a light and chic pastel colour palette or bright and chic colour palette.

The labels will be stuck onto a white pouch. The final design should also include the variety of colour palettes that can be used in AI format with the label. Preferred label measurements in 9cm width, and 11cm height. Our logo is attached.

Beauty and wellness

Health And Wellness

Requirements
Must have
• 2 x labels (front and back)
Front label must include logo, text to include tea type and weight
Back label must include text space to write description
Nice to have
• Simple and chic label design to stick onto a white pouch
Should not have
• Must not have too much graphic and pictures

```html
<!DOCTYPE html>
<html lang="en">
<head>
<meta charset="utf-8">
<title>Fernwood Herbal Tea – Complete Herbal Line</title>
<link rel="stylesheet" href="https://fonts.googleapis.com/css2?family=Cormorant+Garamond:ital,wght@0,500;0,600;1,500&family=Montserrat:wght@400&display=swap">
<style>
  :root {
    --bg: #1b1e1b;
    --cream: #ede6d7;
    --ink: #2b2a26;
    --ink-soft: #5a574f;
    --sketch: rgba(120, 112, 98, 0.13);
    --white: #ffffff;
    --fennel: #939a6c;
    --peppermint: #6bc59b;
    --rose: #ef4e61;
    --echinacea: #cb5aa8;
    --chamomile: #e5cd4f;
    --lemongrass: #b3d246;
    --hibiscus: #db2465;
  }
  * { margin: 0; padding: 0; box-sizing: border-box; }
  html, body { width: 800px; height: 1200px; overflow: hidden; }
  body { background: var(--bg); position: relative; font-family: "Cormorant Garamond", serif; color: var(--ink); }

  .label {
    position: absolute;
    width: 192px;
    height: 288px;
    background: var(--cream);
    overflow: hidden;
  }
  .label__brand {
    position: absolute;
    top: 42px; left: 0; width: 100%;
    text-align: center;
    font-family: "Cormorant Garamond", serif;
    font-weight: 500;
    font-size: 19px;
    color: var(--ink-soft);
    letter-spacing: 0.02em;
  }
  .label__range {
    position: absolute;
    top: 79px; left: 0; width: 100%;
    text-align: center;
    font-family: "Montserrat", sans-serif;
    font-size: 7px;
    letter-spacing: 0.26em;
    color: var(--ink);
    padding-left: 0.26em;
  }
  .label__botanical {
    position: absolute;
    right: 0; top: 110px;
    width: 92px; height: 178px;
    background: linear-gradient(160deg, var(--sketch), rgba(120,112,98,0.04));
  }
  .label__swatch {
    position: absolute;
    left: 48px; top: 160px;
    width: 96px; height: 96px;
    opacity: 0.95;
  }
  .label__flavour {
    position: absolute;
    left: 12px; top: 12px;
    font-family: "Cormorant Garamond", serif;
    font-weight: 600;
    font-size: 9.5px;
    line-height: 1.45;
    letter-spacing: 0.28em;
    color: var(--ink);
    white-space: nowrap;
  }
  .label__flavour small { font-size: 6.5px; letter-spacing: 0.3em; display: block; }
  .label__notes {
    position: absolute;
    left: 28px; top: 63px;
    font-family: "Cormorant Garamond", serif;
    font-style: italic;
    font-size: 4.8px;
    line-height: 1.1;
    color: var(--ink);
  }
  .label__weight {
    position: absolute;
    top: 264px; left: 0; width: 100%;
    text-align: center;
    font-family: "Cormorant Garamond", serif;
    font-weight: 600;
    font-size: 9.5px;
    letter-spacing: 0.06em;
    color: var(--ink);
  }

  .label--fennel { left: 55px; top: 79px; }
  .label--peppermint { left: 310px; top: 79px; }
  .label--rose { left: 560px; top: 79px; width: 196px; height: 293px; }
  .label--echinacea { left: 55px; top: 430px; }
  .label--chamomile { left: 311px; top: 430px; height: 286px; }
  .label--lemongrass { left: 559px; top: 430px; width: 190px; height: 284px; }
  .label--hibiscus { left: 55px; top: 800px; }

  .swatch--fennel { background: var(--fennel); }
  .swatch--peppermint { background: var(--peppermint); }
  .swatch--rose { background: var(--rose); top: 163px; }
  .swatch--echinacea { background: var(--echinacea); }
  .swatch--chamomile { background: var(--chamomile); }
  .swatch--lemongrass { background: var(--lemongrass); left: 47px; }
  .swatch--hibiscus { background: var(--hibiscus); }

  .collection-title {
    position: absolute;
    left: 339px; top: 835px;
    font-family: "Cormorant Garamond", serif;
    font-weight: 500;
    font-size: 52px;
    line-height: 65px;
    letter-spacing: 0.36em;
    color: var(--white);
  }
</style>
</head>
<body>

  <article class="label label--fennel">
    <p class="label__brand">Fernwood</p>
    <p class="label__range">HERBAL TEA</p>
    <div class="label__botanical" role="img" aria-label="Faint botanical line drawing of fennel"></div>
    <div class="label__swatch swatch--fennel">
      <h2 class="label__flavour">FENNEL<br>BLEND</h2>
      <p class="label__notes">Blend<br>Black tea with fresh aroma<br>Tasting Notes<br>Nuts, Orchids, Sweetness</p>
    </div>
    <p class="label__weight">2oz/60g</p>
  </article>

  <article class="label label--peppermint">
    <p class="label__brand">Fernwood</p>
    <p class="label__range">HERBAL TEA</p>
    <div class="label__botanical" role="img" aria-label="Faint botanical line drawing of peppermint leaves"></div>
    <div class="label__swatch swatch--peppermint">
      <h2 class="label__flavour">PEPPERMINT<small>BLEND</small></h2>
      <p class="label__notes">Blend<br>Black tea with fresh aroma<br>Tasting Notes<br>Nuts, Orchids, Sweetness</p>
    </div>
    <p class="label__weight">2oz/60g</p>
  </article>

  <article class="label label--rose">
    <p class="label__brand">Fernwood</p>
    <p class="label__range">HERBAL TEA</p>
    <div class="label__botanical" role="img" aria-label="Faint botanical line drawing of rose blossoms"></div>
    <div class="label__swatch swatch--rose">
      <h2 class="label__flavour">ROSE PETALS<br>BLEND</h2>
      <p class="label__notes">Blend<br>Black tea with fresh aroma<br>Tasting Notes<br>Nuts, Orchids, Sweetness</p>
    </div>
    <p class="label__weight" style="top:268px">2oz/60g</p>
  </article>

  <article class="label label--echinacea">
    <p class="label__brand">Fernwood</p>
    <p class="label__range">HERBAL TEA</p>
    <div class="label__botanical" role="img" aria-label="Faint botanical line drawing of echinacea flowers"></div>
    <div class="label__swatch swatch--echinacea">
      <h2 class="label__flavour">ECHINACEA<br>BLEND</h2>
      <p class="label__notes">Blend<br>Black tea with fresh aroma<br>Tasting Notes<br>Nuts, Orchids, Sweetness</p>
    </div>
    <p class="label__weight">2oz/60g</p>
  </article>

  <article class="label label--chamomile">
    <p class="label__brand">Fernwood</p>
    <p class="label__range">HERBAL TEA</p>
    <div class="label__botanical" role="img" aria-label="Faint botanical line drawing of chamomile flowers"></div>
    <div class="label__swatch swatch--chamomile" style="top:158px">
      <h2 class="label__flavour">CHAMOMILE<br>BLEND</h2>
      <p class="label__notes">Blend<br>Black tea with fresh aroma<br>Tasting Notes<br>Nuts, Orchids, Sweetness</p>
    </div>
    <p class="label__weight" style="top:262px">2oz/60g</p>
  </article>

  <article class="label label--lemongrass">
    <p class="label__brand">Fernwood</p>
    <p class="label__range">HERBAL TEA</p>
    <div class="label__botanical" role="img" aria-label="Faint botanical line drawing of lemongrass stalks"></div>
    <div class="label__swatch swatch--lemongrass" style="top:158px">
      <h2 class="label__flavour">LEMONGRASS<br>BLEND</h2>
      <p class="label__notes">Blend<br>Black tea with fresh aroma<br>Tasting Notes<br>Nuts, Orchids, Sweetness</p>
    </div>
    <p class="label__weight" style="top:261px">2oz/60g</p>
  </article>

  <article class="label label--hibiscus">
    <p class="label__brand">Fernwood</p>
    <p class="label__range">HERBAL TEA</p>
    <div class="label__botanical" role="img" aria-label="Faint botanical line drawing of a hibiscus flower"></div>
    <div class="label__swatch swatch--hibiscus">
      <h2 class="label__flavour">HIBISCUS<br>BLEND</h2>
      <p class="label__notes">Blend<br>Black tea with fresh aroma<br>Tasting Notes<br>Nuts, Orchids, Sweetness</p>
    </div>
    <p class="label__weight">2oz/60g</p>
  </article>

  <h1 class="collection-title">COMPLETE<br>HERBAL<br>LINE</h1>

</body>
</html>
```